Meditation class design

I need a flyer design for a new meditation class based in Narellan NSW. The information that I want on the flyer is:
'THE QUIET RIVER'
Awaken to your purpose. Guiding you to your true divinity.
Allow yourself to invest time for YOU.
Clear the mind with stillness and learn to live in the NOW.
BENEFITS: Balance
Healing the Mind, Body & Spirit
Creates Peace & calmness
Self development
Happiness
Letting go to what is
Clearer mind
Keeps you looking young
Answers
Enriching your life by excepting & embracing who you are
Picture in the whole background of a person sitting down crossed legged looking into the sun with a butterfly around in the distance. Colours to use is shades of purple, white, shades of pink.
Updates

I don't need any more designs for my flyer. Can anyone help me to get my file that Tam has created for me.  I have downloaded it but can't see it.

Thank you

REGARDS

BRENT HOLLOWAY

Requirements
Must have
• TIME: 10am to 11am
WHERE: Coastal Fitness Hall, Unit 5
3-7 Pemberton Vale Street
Narellan NSW
PRICE: $15.00

'ENHANCING THE QUALITY OF YOUR LIFE & THOSE AROUND YOU'

Contact Brent on 0432 918 256
Email: quietriver@mailvista.net
Facebook: Gentle Shoreline Wellness

```html
<!DOCTYPE html>
<html lang="en">
<head>
<meta charset="utf-8">
<title>The Quiet River – Meditation Class Flyer</title>
<link rel="stylesheet" href="https://fonts.googleapis.com/css2?family=Tinos:ital,wght@0,400;1,400;1,700&family=Arimo:wght@400;500&display=swap">
<style>
  :root {
    --page-bg: #000000;
    --band-purple: #432f8c;
    --band-deep: #3a2780;
    --sky-light: #e9e3f4;
    --sky-mid: #9a86c8;
    --sky-deep: #5b3f9c;
    --field: #5c2236;
    --panel-pink: rgba(190, 70, 160, 0.72);
    --panel-edge: #e59ad2;
    --wave-pink: #c98cc9;
    --cream-text: #f6e9a8;
    --benefit-yellow: #f4e04b;
    --white: #ffffff;
    --daisy-centre: #f2c230;
  }
  * { margin: 0; padding: 0; box-sizing: border-box; }
  html, body { width: 964px; height: 1200px; overflow: hidden; background: var(--page-bg); }
  .flyer {
    position: absolute; left: 79px; top: 83px; width: 793px; height: 1021px;
    overflow: hidden; background: var(--band-deep);
  }
  .header-band {
    position: absolute; left: 0; top: 0; width: 100%; height: 107px;
    background: var(--band-purple);
    display: flex; align-items: center; justify-content: center;
    font-family: "Tinos", serif; color: var(--white);
    font-size: 31px; line-height: 38px; text-align: center; letter-spacing: 0.5px;
  }
  .header-band h1 { font: inherit; }
  .scene {
    position: absolute; left: 0; top: 107px; width: 100%; height: 760px;
    background:
      radial-gradient(ellipse 340px 260px at 560px 120px, rgba(255,255,255,0.9), rgba(255,255,255,0) 70%),
      radial-gradient(ellipse 260px 380px at 600px 520px, rgba(245,245,250,0.55), rgba(255,255,255,0) 75%),
      linear-gradient(180deg, var(--sky-deep) 0%, var(--sky-mid) 35%, var(--sky-light) 55%, var(--sky-mid) 68%, var(--field) 82%, var(--field) 100%);
  }
  .panel { position: absolute; left: 20px; width: 351px; }
  .panel-shape { position: absolute; left: 0; top: 0; width: 100%; height: 100%; }
  .panel-list {
    position: relative; list-style: none;
    font-family: "Tinos", serif; font-style: italic; color: var(--cream-text);
  }
  .panel-list li { position: relative; padding-left: 38px; }
  .daisy { position: absolute; left: 8px; top: 0; width: 22px; height: 22px; }
  .intro-panel { top: 126px; height: 222px; }
  .intro-panel .panel-list { padding: 46px 14px 0 12px; font-size: 17px; line-height: 21px; }
  .intro-panel li { margin-bottom: 14px; }
  .benefits-panel { top: 385px; height: 373px; }
  .benefits-title {
    position: relative; padding: 60px 0 0 46px;
    font-family: "Tinos", serif; font-style: italic; font-weight: 700;
    font-size: 23px; letter-spacing: 1px; color: var(--benefit-yellow);
  }
  .benefits-panel .panel-list { padding: 6px 4px 0 12px; font-size: 16.5px; }
  .benefits-panel li { height: 32px; line-height: 22px; }
  .benefits-panel li.gap { margin-top: 6px; }
  .benefits-panel .daisy { width: 20px; height: 20px; }
  .footer-wave { position: absolute; left: 0; top: 810px; width: 100%; height: 211px; }
  .contact, .details {
    position: absolute; font-family: "Arimo", sans-serif; color: var(--white); font-style: normal;
  }
  .contact { left: 25px; top: 887px; font-size: 18.5px; line-height: 26px; }
  .contact .phone { font-size: 29px; line-height: 34px; margin-top: 2px; }
  .details { left: 480px; top: 882px; font-size: 18.5px; line-height: 25px; font-weight: 500; }
</style>
</head>
<body>
<main class="flyer">
  <header class="header-band">
    <h1>ENHANCING THE QUALITY OF<br>YOUR LIFE &amp; THOSE AROUND YOU</h1>
  </header>

  <div class="scene" role="img" aria-label="Photograph of a woman in white sitting cross-legged in meditation, hands together, under a glowing purple sky with a tree, a lavender field and butterflies"></div>

  <section class="panel intro-panel">
    <svg class="panel-shape" viewBox="0 0 351 222" preserveAspectRatio="none" aria-hidden="true">
      <path d="M6 14 Q120 -4 230 10 T346 12 L346 206 Q240 226 140 208 T6 210 Z" fill="var(--panel-pink)" stroke="var(--panel-edge)" stroke-width="2"/>
    </svg>
    <ul class="panel-list">
      <li><svg class="daisy" viewBox="0 0 22 22" aria-hidden="true"><circle cx="11" cy="11" r="10" fill="var(--white)"/><circle cx="11" cy="11" r="4.5" fill="var(--daisy-centre)"/></svg>Awaken to your purpose. Guiding you to your true divinity.</li>
      <li><svg class="daisy" viewBox="0 0 22 22" aria-hidden="true"><circle cx="11" cy="11" r="10" fill="var(--white)"/><circle cx="11" cy="11" r="4.5" fill="var(--daisy-centre)"/></svg>Allow yourself to invest time for YOU.</li>
      <li><svg class="daisy" viewBox="0 0 22 22" aria-hidden="true"><circle cx="11" cy="11" r="10" fill="var(--white)"/><circle cx="11" cy="11" r="4.5" fill="var(--daisy-centre)"/></svg>Clear the mind with stillness and learn to live in the NOW.</li>
    </ul>
  </section>

  <section class="panel benefits-panel">
    <svg class="panel-shape" viewBox="0 0 351 373" preserveAspectRatio="none" aria-hidden="true">
      <path d="M6 22 Q110 -6 220 14 T346 18 L346 356 Q250 376 150 356 T6 360 Z" fill="var(--panel-pink)" stroke="var(--panel-edge)" stroke-width="2"/>
    </svg>
    <h2 class="benefits-title">BENEFITS</h2>
    <ul class="panel-list">
      <li><svg class="daisy" viewBox="0 0 22 22" aria-hidden="true"><circle cx="11" cy="11" r="10" fill="var(--white)"/><circle cx="11" cy="11" r="4.5" fill="var(--daisy-centre)"/></svg>Balance Healing the Mind, Body &amp; Spirit</li>
      <li><svg class="daisy" viewBox="0 0 22 22" aria-hidden="true"><circle cx="11" cy="11" r="10" fill="var(--white)"/><circle cx="11" cy="11" r="4.5" fill="var(--daisy-centre)"/></svg>Creates Peace &amp; calmness</li>
      <li><svg class="daisy" viewBox="0 0 22 22" aria-hidden="true"><circle cx="11" cy="11" r="10" fill="var(--white)"/><circle cx="11" cy="11" r="4.5" fill="var(--daisy-centre)"/></svg>Self development</li>
      <li><svg class="daisy" viewBox="0 0 22 22" aria-hidden="true"><circle cx="11" cy="11" r="10" fill="var(--white)"/><circle cx="11" cy="11" r="4.5" fill="var(--daisy-centre)"/></svg>Happiness</li>
      <li class="gap"><svg class="daisy" viewBox="0 0 22 22" aria-hidden="true"><circle cx="11" cy="11" r="10" fill="var(--white)"/><circle cx="11" cy="11" r="4.5" fill="var(--daisy-centre)"/></svg>Letting go to what isClearer mind</li>
      <li><svg class="daisy" viewBox="0 0 22 22" aria-hidden="true"><circle cx="11" cy="11" r="10" fill="var(--white)"/><circle cx="11" cy="11" r="4.5" fill="var(--daisy-centre)"/></svg>Keeps you looking young</li>
    </ul>
  </section>

  <svg class="footer-wave" viewBox="0 0 793 211" preserveAspectRatio="none" aria-hidden="true">
    <path d="M0 0 Q220 40 430 34 T793 36 L793 211 L0 211 Z" fill="var(--wave-pink)"/>
    <path d="M0 14 Q220 52 430 46 T793 46 L793 211 L0 211 Z" fill="var(--band-deep)"/>
  </svg>

  <address class="contact">
    <p>Contact Brent on</p>
    <p class="phone">0432 918 256</p>
    <p>Email: quietriver@mailvista.net</p>
    <p>Facebook: Gentle Shoreline Wellness</p>
  </address>

  <div class="details">
    <p>TIME: 10am to 11am</p>
    <p>Coastal Fitness Hall, Unit 5</p>
    <p>3-7 Pemberton Vale Street</p>
    <p>Narellan NSW</p>
    <p>PRICE: $15.00</p>
  </div>
</main>
</body>
</html>
```